A standard Business and Stock Market Website

We are looking for a well designed and attractive website design which deals on the day to day business activities and stock market performance across the globe.

A good reference website for my proposed website is http://quillharbor.com and http://vkp.com

We are basically featuring the leading stock markets such as Pell marsh stock market and others. The Business name is Quarry lane.
I require very bright colors such as blue, green, black, golden.

Easy nagivating of the website is require and the design should also be responsive on mobile devices.

Designs for three pages. The first design should be for the home page, the second for the Economy/ stockmarkets, Third, business and tech. The home image would also feature stocks, economy, business, tech.

```html
<!DOCTYPE html>
<html lang="en">
<head>
<meta charset="utf-8">
<title>Quarry Lane — Business &amp; Markets</title>
<link href="https://fonts.googleapis.com/css2?family=Lato:ital,wght@0,300;0,400;0,700;1,400&display=swap" rel="stylesheet">
<style>
:root{
  --black:#000;
  --bar:#0d0d0d;
  --line:#2a2a2a;
  --gold:#f5a623;
  --navy:#2b3990;
  --paper:#f2f2f2;
  --white:#fff;
  --ink:#111;
  --muted:#9a9a9a;
  --soft:#c9c9c9;
  --red:#e53935;
  --green:#43a047;
}
*{box-sizing:border-box;margin:0;padding:0}
html,body{width:1121px;height:1200px;overflow:hidden}
body{font-family:'Lato',sans-serif;background:var(--paper);position:relative;color:var(--ink)}
a{color:inherit;text-decoration:none}
.abs{position:absolute}
.top{position:absolute;left:0;top:0;width:1121px;height:446px;background:var(--black);color:var(--white)}
.ticker{height:20px;background:var(--bar);display:flex;justify-content:center;gap:34px;align-items:center;font-size:6.5px;color:var(--white)}
.ticker .dn{color:var(--red)} .ticker .up{color:var(--green)}
.header{position:absolute;top:20px;left:168px;width:784px;height:40px;display:flex;align-items:center}
.brand{display:flex;align-items:center;gap:5px;font-size:20px;font-weight:300;color:var(--white)}
.brand .mark{width:14px;height:14px;border:1.5px solid var(--white)}
.vsep{width:1px;height:16px;background:var(--gold);margin:0 10px}
.promo{font-size:6px;line-height:9px;color:var(--white);font-weight:700}
.promo span{color:var(--gold);font-weight:400}
.nav{display:flex;gap:14px;font-size:6.5px;margin-left:6px}
.nav .on{color:var(--gold)}
.subscribe{color:var(--gold);font-size:6.5px;font-weight:700;margin:0 22px}
.util{position:absolute;top:60px;left:0;width:1121px;height:21px;border-top:1px solid var(--line);border-bottom:1px solid var(--line);font-size:5.5px}
.util .login{position:absolute;left:168px;width:107px;height:19px;border-left:1px solid var(--line);border-right:1px solid var(--line);display:flex;align-items:center;justify-content:center;gap:6px;font-weight:700}
.util .field{position:absolute;height:19px;border-left:1px solid var(--line);display:flex;align-items:center;justify-content:space-between;padding:0 7px 0 13px}
.sec-title{font-size:10px;font-weight:700;color:var(--white);display:flex;align-items:center;gap:3px}
.sec-title i{width:7px;height:7px;border-radius:50%;background:var(--gold);display:inline-block}
.news-l h4{font-size:7px;font-weight:400;line-height:9px}
.news-l p{font-size:5.6px;line-height:8px;color:#cfcfcf}
.meta{font-size:4.8px;color:var(--white);display:flex;gap:3px;align-items:center;margin-top:1px}
.meta b{width:5px;height:5px;border:1px solid var(--gold);border-radius:50%}
.bullets{font-size:5.6px;line-height:8px;color:#cfcfcf;margin-top:10px}
.bullets span{color:var(--gold)}
.divider{border-bottom:1px solid var(--line);margin:8px 0 11px}
.ph{background:var(--navy);color:var(--white);display:flex;align-items:center;justify-content:center;font-weight:400;letter-spacing:.5px}
.hero-kicker{font-size:9.5px;font-weight:700;display:flex;align-items:center;gap:3px}
.hero-kicker i{width:6px;height:6px;background:var(--gold);transform:rotate(45deg)}
.hero h1{font-size:17.5px;font-weight:400;margin:9px 0 8px}
.hero p{font-size:5.7px;line-height:7.8px;color:#cfcfcf}
.hero p span{color:var(--gold)}
.tabs{display:flex;gap:15px;font-size:6px;color:#ddd;margin:11px 0 0 15px}
.tabs .on{color:var(--gold)}
.mkt{width:214px;font-size:5.8px;border-collapse:collapse}
.mkt td{height:15px;padding:0 6px}
.mkt tr:nth-child(odd){background:#151515}
.mkt .n{text-align:right} .mkt .r{text-align:right;color:var(--red)}
.op .entry{margin-top:6px}
.op a{display:block;font-size:7px;line-height:10px;color:var(--white)}
.op a::after{content:"";display:inline-block;width:6px;height:1.5px;background:var(--gold);margin-left:4px;vertical-align:middle}
.op em{display:block;font-size:5.6px;line-height:8px;color:var(--muted)}
.card{position:absolute;background:var(--white)}
.side-item h4{font-size:7px;line-height:9px;font-weight:700;color:var(--ink)}
.side-item p{font-size:5.7px;line-height:8px;color:var(--muted);margin-top:6px}
.side-item .meta{color:var(--ink)}
.side-item .meta b{border-color:var(--navy)}
.side-item{border-bottom:1px solid #ddd;padding-bottom:8px;margin-bottom:7px;height:146px}
.story{position:absolute;left:11px;display:flex;gap:16px}
.story .txt{width:190px}
.story h3{font-size:9.3px;line-height:12.6px;font-weight:700}
.story p{font-size:5.8px;line-height:8px;color:#333;margin-top:3px}
.story .ago{font-size:5.7px;color:var(--muted);margin-top:9px}
.story .by{font-size:5.7px;color:var(--muted);margin-top:9px}
.story .by span{color:var(--navy);margin-right:10px}
.latest{padding:10px 11px}
.latest .sec-title{color:var(--ink)}
.latest .item{border-bottom:1px solid #ddd;padding:6px 3px 6px;font-size:6.8px;line-height:10px;font-weight:700;min-height:34px}
.latest .item em{font-size:5.6px;color:var(--soft);font-weight:400}
.more{font-size:6.5px;color:var(--gold);font-weight:700;font-style:italic;margin:8px 3px 0;display:block}
</style>
</head>
<body>
<section class="top">
  <div class="ticker">
    <span>QLIA <b class="dn">▼</b> 19762.60 -0.29%</span>
    <span>QL 500 <b class="dn">▼</b> 2238.83 - 0.46%</span>
    <span>Norvale Comp <b class="dn">▼</b> 5383.12 -0.90%</span>
    <span>U.S. 10 Yr 0/32 Yield &nbsp;2.445%</span>
    <span>Crude Oil <b class="up">▲</b> 53.89 &nbsp;0.22%</span>
    <span>EURO <b class="up">▲</b> 1.0519 &nbsp;0.27%</span>
  </div>
  <header class="header">
    <a class="brand" href="#"><span class="mark"></span>Quarry Lane</a>
    <span class="vsep"></span>
    <div class="promo">INVEST WITH CALDWELL<br><span>FREE for 14 Days ▸</span></div>
    <span class="vsep"></span>
    <nav class="nav">
      <a class="on">Home</a><a>World</a><a>U.S.</a><a>Politics</a><a>Economy</a><a>Business</a><a>Tech</a><a>Markets</a><a>Opinion</a><a>Arts</a><a>Life</a><a>Real Estate</a>
    </nav>
    <span class="vsep" style="margin-left:26px;margin-right:0"></span>
    <a class="subscribe">SUBSCRIBE</a>
    <span class="vsep" style="background:#fff;margin:0"></span>
  </header>
  <div class="util">
    <div class="login">LOGIN <span>|</span> GET ALERTS <span style="color:var(--gold)">›</span></div>
    <div class="field" style="left:674px;width:117px">Search <span style="color:var(--gold)">○</span></div>
    <div class="field" style="left:791px;width:161px;border-right:1px solid var(--line)">Search Keyword <span style="color:var(--gold)">○</span></div>
  </div>

  <aside class="abs news-l" style="left:168px;top:90px;width:107px">
    <div class="sec-title"><i></i>WHAT'S NEWS</div>
    <div style="margin-top:9px">
      <h4>Orlan Declines to Retaliate in Move Praised by Marsden</h4>
      <p>President Viktor Orlan said Russia wouldn't expel any U.S. diplomats in response to the U.S. decision to kick out dozens of alleged Russian operatives, an unexpected move that drew.</p>
      <div class="meta"><b></b>3543</div>
      <div class="bullets"><span>•</span> Behind Russia's Cyber Strategy<br><span>•</span> U.S. Punishes Russia Over Cyberattacks<br><span>•</span> Marsden Plan to Partner With Russia Faces Bigger Hurdle</div>
    </div>
    <div class="divider"></div>
    <h4>White House Transition Turns Tense</h4>
    <p>President Brandon Oakes and his successor Dale Marsden are making moves that tread on each other's turf and complicate the other's agenda, creating one of the messiest White House transitions in recent years.</p>
    <div class="meta"><b></b>3543 &nbsp;2 hours ago</div>
    <div class="divider"></div>
    <h4>White House Transition Turns Tense</h4>
    <p style="font-size:4.6px;line-height:8px">President Brandon Oakes and his successor Dale Marsden are making moves that tread on each other's turf and complicate the other's agenda, creating.</p>
    <div class="meta"><b></b>3543 &nbsp;2 hours ago</div>
  </aside>

  <article class="abs hero" style="left:292px;top:90px;width:427px">
    <div class="ph" role="img" aria-label="Lead story photograph" style="height:206px;font-size:34px">IMAGE</div>
    <div class="hero-kicker" style="margin-top:11px"><i></i>SPIN INTERVIEW</div>
    <h1>Orlan Declines to Retaliate in Move Praised by Marsden</h1>
    <p>Lorem Ipsum is simply dummy text of the printing and typesetting industry. Lorem Ipsum has been the industry's standard dummy text ever since the 1500s, when an unknown printer took a galley of type and scrambled it to make a type specimen book. It has survived not only five centuries, but also the leap into electronic typesetting, remaining essentially unchanged. It was popularised in the 1960s with the release of Typeset sheets containing Lorem Ipsum passages, and more recently with desktop publishing software like Page layout including versions of Lorem Ipsum.<br><span>7 minutes ago</span></p>
  </article>

  <aside class="abs" style="left:736px;top:90px;width:214px">
    <div class="sec-title"><i></i>MARKETS</div>
    <div class="tabs"><span class="on">U.S.</span><span>EUROPE</span><span>ASIA</span><span>FX</span><span>RATES</span><span>FUTURES</span></div>
    <svg width="214" height="90" viewBox="0 0 214 90" style="margin-top:14px;display:block">
      <g fill="#1a1a1a"><rect y="12" width="214" height="9"/><rect y="30" width="214" height="9"/><rect y="48" width="214" height="9"/><rect y="66" width="214" height="9"/></g>
      <polyline fill="none" stroke="#fff" stroke-width=".6" stroke-dasharray="1.5 1.5" points="0,56 16,38 26,46 32,40 60,76 76,60 88,72 118,32 142,62 158,48 174,66 214,12"/>
      <polyline fill="none" stroke="var(--gold)" stroke-width=".8" stroke-dasharray="1 1.5" points="0,60 16,41 26,49 32,43 60,79 76,63 88,75 118,35 142,65 158,51 174,69 214,5"/>
      <g fill="var(--gold)"><circle cx="16" cy="38" r="2.2"/><circle cx="26" cy="46" r="2.2"/><circle cx="32" cy="40" r="2.2"/><circle cx="60" cy="76" r="2.2"/><circle cx="76" cy="60" r="2.2"/><circle cx="88" cy="72" r="2.2"/><circle cx="118" cy="32" r="2.2"/><circle cx="142" cy="62" r="2.2"/><circle cx="158" cy="48" r="2.2"/><circle cx="174" cy="66" r="2.2"/></g>
    </svg>
    <table class="mkt" style="margin-top:3px">
      <tr><td>QLIA</td><td class="n">19762.60</td><td class="r">-57.18</td><td class="r">-0.29%</td></tr>
      <tr><td>QL 500</td><td class="n">2238.83</td><td class="r">-10.43</td><td class="r">-0.46%</td></tr>
      <tr><td>Norvale Comp</td><td class="n">5383.12</td><td class="r">-48.97</td><td class="r">-0.29%</td></tr>
      <tr><td>Ruskin 2K</td><td class="n">1357.13</td><td class="r">-6.05</td><td class="r">-0.46%</td></tr>
      <tr><td>QL Total Mkt</td><td class="n">23276.73</td><td class="r">-103.80</td><td class="r">-0.44%</td></tr>
    </table>
    <div style="display:flex;justify-content:space-between;font-size:4.8px;color:var(--muted);padding:6px 6px;border-top:1px solid var(--line);margin-top:3px"><span>Dec 30 '16, 4:45 PM EST</span><span>MARKETS</span></div>
    <div class="sec-title" style="margin-top:10px"><i></i>OPINION</div>
    <div class="op">
      <div class="entry"><a>Asia's Rising Terror Risk</a><em>Review &amp; Outlook</em></div>
      <div class="entry"><a>The Backlash Against Burm</a><em>Review &amp; Outlook</em></div>
      <div class="entry"><a>A United Front for a More Open China</a><em>By Dennis Dorrow and Pierre Lacombe | Opinion</em></div>
    </div>
  </aside>
</section>

<div class="card" style="left:169px;top:458px;width:106px;height:643px;padding:4px 7px">
  <div class="side-item"><h4>White House Transition Turns Tense</h4><div class="ph" role="img" aria-label="Story photograph" style="height:39px;font-size:10px;margin-top:3px">IMAGE</div><p>President Brandon Oakes and his successor Dale Marsden are making moves that tread on each other's turf and complicate the other's agenda, creating one of the messiest White House transitions in recent years.</p><div class="meta"><b></b>15 &nbsp;3 hours ago</div></div>
  <div class="side-item"><h4>White House Transition Turns Tense</h4><div class="ph" role="img" aria-label="Story photograph" style="height:39px;font-size:10px;margin-top:3px">IMAGE</div><p>President Brandon Oakes and his successor Dale Marsden are making moves that tread on each other's turf and complicate the other's agenda, creating one of the messiest White House transitions in recent years.</p><div class="meta"><b></b>15 &nbsp;3 hours ago</div></div>
  <div class="side-item"><h4>White House Transition Turns Tense</h4><div class="ph" role="img" aria-label="Story photograph" style="height:39px;font-size:10px;margin-top:3px">IMAGE</div><p>President Brandon Oakes and his successor Dale Marsden are making moves that tread on each other's turf and complicate the other's agenda, creating one of the messiest White House transitions in recent years.</p><div class="meta"><b></b>15 &nbsp;3 hours ago</div></div>
  <div class="side-item"><h4>White House Transition Turns Tense</h4><div class="ph" role="img" aria-label="Story photograph" style="height:39px;font-size:10px;margin-top:3px">IMAGE</div><p>President Brandon Oakes and his successor Dale Marsden are making moves that tread on each other's turf and complicate the other's agenda, creating one of the messiest White House transitions in recent years.</p><div class="meta"><b></b>15 &nbsp;3 hours ago</div></div>
</div>

<div class="card" style="left:291px;top:458px;width:428px;height:599px">
  <div class="story" style="top:10px"><div class="ph" role="img" aria-label="Market review photograph" style="width:188px;height:96px;font-size:17px">IMAGE</div><div class="txt"><h3>Week in Review: Marsden Rally Fizzles but Stocks End 2016 With Big Gains</h3><p>The post-Marsden rally came to an end this week, as the index missed its 20,000 milestone and stocks ended lower Friday, while finishing 2016 with big gains.</p><div class="ago">7 minutes ago</div><div class="by"><span>Vera Yates</span> I &nbsp;&nbsp; Dec 30, 2016 6:10 PM EST</div></div></div>
  <div class="story" style="top:130px"><div class="ph" role="img" aria-label="Market review photograph" style="width:188px;height:96px;font-size:17px">IMAGE</div><div class="txt"><h3>Week in Review: Marsden Rally Fizzles but Stocks End 2016 With Big Gains</h3><p>The post-Marsden rally came to an end this week, as the index missed its 20,000 milestone and stocks ended lower Friday, while finishing 2016 with big gains.</p><div class="ago">7 minutes ago</div><div class="by"><span>Vera Yates</span> I &nbsp;&nbsp; Dec 30, 2016 6:10 PM EST</div></div></div>
  <div class="story" style="top:250px"><div class="ph" role="img" aria-label="Market review photograph" style="width:188px;height:96px;font-size:17px">IMAGE</div><div class="txt"><h3>Week in Review: Marsden Rally Fizzles but Stocks End 2016 With Big Gains</h3><p>The post-Marsden rally came to an end this week, as the index missed its 20,000 milestone and stocks ended lower Friday, while finishing 2016 with big gains.</p><div class="ago">7 minutes ago</div><div class="by"><span>Vera Yates</span> I &nbsp;&nbsp; Dec 30, 2016 6:10 PM EST</div></div></div>
  <div class="story" style="top:370px"><div class="ph" role="img" aria-label="Market review photograph" style="width:188px;height:96px;font-size:17px">IMAGE</div><div class="txt"><h3>Week in Review: Marsden Rally Fizzles but Stocks End 2016 With Big Gains</h3><p>The post-Marsden rally came to an end this week, as the index missed its 20,000 milestone and stocks ended lower Friday, while finishing 2016 with big gains.</p><div class="ago">7 minutes ago</div><div class="by"><span>Vera Yates</span> I &nbsp;&nbsp; Dec 30, 2016 6:10 PM EST</div></div></div>
  <div class="story" style="top:490px"><div class="ph" role="img" aria-label="Market review photograph" style="width:188px;height:96px;font-size:17px">IMAGE</div><div class="txt"><h3>Week in Review: Marsden Rally Fizzles but Stocks End 2016 With Big Gains</h3><p>The post-Marsden rally came to an end this week, as the index missed its 20,000 milestone and stocks ended lower Friday, while finishing 2016 with big gains.</p><div class="ago">7 minutes ago</div><div class="by"><span>Vera Yates</span> I &nbsp;&nbsp; Dec 30, 2016 6:10 PM EST</div></div></div>
</div>

<div class="card latest" style="left:736px;top:458px;width:216px;height:183px">
  <div class="sec-title"><i></i>LATEST NEWS</div>
  <div class="item">Traders Are Cleaning Out Their Portfolios: Rev Marlin's Best Blog <em>9:00 PM | Quarry Lane</em></div>
  <div class="item">Clean the Slate for the New Year: Best of Kessel <em>9:00 PM | Quarry Lane</em></div>
  <div class="item">Traders Are Cleaning Out Their Portfolios: Rev Marlin's Best Blog <em>9:00 PM | Quarry Lane</em></div>
  <div class="item">Clean the Slate for the New Year: Best of Kessel <em>9:00 PM | Quarry Lane</em></div>
  <a class="more">MORE NEWS ›</a>
</div>
<div class="card latest" style="left:736px;top:652px;width:216px;height:183px">
  <div class="sec-title"><i></i>LATEST NEWS</div>
  <div class="item">Traders Are Cleaning Out Their Portfolios: Rev Marlin's Best Blog <em>9:00 PM | Quarry Lane</em></div>
  <div class="item">Clean the Slate for the New Year: Best of Kessel <em>9:00 PM | Quarry Lane</em></div>
  <div class="item">Traders Are Cleaning Out Their Portfolios: Rev Marlin's Best Blog <em>9:00 PM | Quarry Lane</em></div>
  <div class="item">Clean the Slate for the New Year: Best of Kessel <em>9:00 PM | Quarry Lane</em></div>
  <a class="more">MORE NEWS ›</a>
</div>
</body>
</html>
```